Design of Stationery (Business Card, Letterhead and Envelope) for Investment Company
Kestrelmoor Capital Associates Limited
Design of Stationery (Business Card, Letterhead and Envelope) for Investment Company - Financial Services
Creative Brief
Simple
Tunde A. Ibekwe
Director
7C, Dunmore Crescent, Osapa Garden Estate, Lekki Peninsula, Lagos
tunde@kestrelmoorng.example
www.kestrelmoorng.example
RC 458290
The back of the business card should have the logo of the company on navy blue background - please see the logo uploaded. Below the logo should be the words: "INVESTMENTS. ADVICE. VALUE CREATION".

```html
<!DOCTYPE html>
<html lang="en">
<head>
<meta charset="utf-8">
<title>Kestrelmoor Capital Associates Limited – Business Card</title>
<link href="https://fonts.googleapis.com/css2?family=Cinzel:wght@500&family=Open+Sans:wght@400;600&display=swap" rel="stylesheet">
<style>
  :root{
    --navy:#34456f;
    --navy-deep:#26345a;
    --grey:#9a9ea6;
    --grey-light:#d7d9dd;
    --ink:#3d4350;
    --paper:#ffffff;
    --backdrop:#eceae6;
  }
  *{margin:0;padding:0;box-sizing:border-box}
  html,body{width:1200px;height:828px;overflow:hidden}
  body{background:var(--backdrop);position:relative;font-family:"Open Sans",sans-serif;color:var(--ink)}
  .card{position:absolute;top:260px;width:540px;height:308px;background:var(--paper);overflow:hidden;box-shadow:0 6px 18px rgba(0,0,0,.12)}
  .card--back{left:40px}
  .card--front{left:620px}
  .card svg{position:absolute;inset:0}
  .wordmark{position:absolute;font-family:"Cinzel",serif;font-weight:500;color:var(--navy);text-align:center;line-height:1}
  .card--back .wordmark{right:34px;top:46px}
  .wordmark__main{display:block;font-size:30px;letter-spacing:1px}
  .wordmark__sub{display:block;font-size:10.5px;letter-spacing:2.6px;margin-top:5px}
  .card--front .brand{position:absolute;left:50px;top:118px;display:flex;flex-direction:column;align-items:center}
  .brand__square{width:40px;height:40px;background:var(--navy);margin-bottom:12px}
  .card--front .wordmark{position:static}
  .card--front .wordmark__main{font-size:26px}
  .card--front .wordmark__sub{font-size:9px;letter-spacing:2.2px}
  .contact{position:absolute;left:300px;top:42px;font-size:10.5px;line-height:1.45}
  .contact__name{font-size:14px;font-weight:600;color:var(--navy);letter-spacing:.5px;text-transform:uppercase}
  .contact__role{margin-bottom:8px}
  .contact__row{display:flex;align-items:center;gap:6px;margin-top:3px}
  .contact__row svg{position:static;width:10px;height:10px;flex:none}
  .website{position:absolute;right:26px;bottom:22px;color:var(--paper);font-size:11px;letter-spacing:.5px}
</style>
</head>
<body>

<section class="card card--back" aria-label="Business card back">
  <svg viewBox="0 0 540 308" width="540" height="308" aria-hidden="true">
    <path d="M0,0 H200 C150,90 160,210 300,308 H0 Z" fill="var(--grey-light)"/>
    <path d="M0,0 H178 C128,90 136,210 262,308 H0 Z" fill="var(--paper)"/>
    <path d="M0,0 H160 C108,95 112,215 232,308 H0 Z" fill="var(--navy)"/>
    <path d="M160,0 C108,95 112,215 232,308" fill="none" stroke="var(--navy-deep)" stroke-width="2"/>
  </svg>
  <div class="wordmark">
    <span class="wordmark__main">KESTRELMOOR</span>
    <span class="wordmark__sub">CAPITAL ASSOCIATES</span>
  </div>
</section>

<section class="card card--front" aria-label="Business card front">
  <svg viewBox="0 0 540 308" width="540" height="308" aria-hidden="true">
    <path d="M540,120 C470,215 340,268 170,308" fill="none" stroke="var(--grey)" stroke-width="3"/>
    <path d="M540,150 C460,240 330,285 210,308 H540 Z" fill="var(--grey-light)"/>
    <path d="M540,168 C465,250 345,292 250,308 H540 Z" fill="var(--navy)"/>
  </svg>

  <div class="brand">
    <span class="brand__square"></span>
    <div class="wordmark">
      <span class="wordmark__main">KESTRELMOOR</span>
      <span class="wordmark__sub">CAPITAL ASSOCIATES</span>
    </div>
  </div>

  <div class="contact">
    <p class="contact__name">Tunde A. Ibekwe</p>
    <p class="contact__role">Managing Director</p>
    <p>7C, Dunmore Crescent</p>
    <p>Osapa Garden Estate, Lagos</p>
    <p class="contact__row">
      <svg viewBox="0 0 10 10"><rect x="0.5" y="1.5" width="9" height="7" fill="none" stroke="var(--navy)"/><path d="M0.5,1.5 L5,5.5 L9.5,1.5" fill="none" stroke="var(--navy)"/></svg>
      tunde@kestrelmoorng.example
    </p>
    <p class="contact__row">
      <svg viewBox="0 0 10 10"><path d="M2,0.5 L4,3 L3,4.2 C3.8,5.8 4.6,6.6 6,7.2 L7.2,6.2 L9.5,8.2 L8.2,9.5 C4,9 1,6 0.5,1.8 Z" fill="var(--navy)"/></svg>
      090 555 0142
    </p>
  </div>

  <p class="website">www.kestrelmoorng.example</p>
</section>

</body>
</html>
```